Professional Modern Website Design

We are a premium IT services provider to the financial industry based in London. Our company is called Veltra our current holding page is www.veltra-example.co.uk. We require a new website to match our new corporate identity. This project is for the design phase only. Development will be handled in-house. I have attached examples of wire frames we have developed (although open to suggestions for improvement) Our brand document that should demonstrate current brand, inc how we communicate to potential clients and finally mostly completed web-content.
We are looking for designers that can create something that sets us apart from our competitors.
Target Market(s)
IT Decision makers in Finance companies such as; hedge funds, private investment banks etc
Industry/Entity Type
Financial
Number of Pages Required
5+ page
Requirements
Must have
- hexagon elements in the design, unique design.
Nice to have
- Blog and social media feeds
Should not have
- Should not resemble a downloaded template

```html
<!DOCTYPE html>
<html lang="en">
<head>
<meta charset="utf-8">
<title>Veltra – IT Services for Finance</title>
<link href="https://fonts.googleapis.com/css2?family=Raleway:wght@300;400;500;600;700&display=swap" rel="stylesheet">
<style>
:root{
  --orange:#f37021;
  --orange-deep:#d9581a;
  --amber:#fbb117;
  --charcoal:#1d1d1d;
  --slate:#4a4a4a;
  --ink:#222;
  --muted:#444;
  --line:#d6d6d6;
  --footer:#111;
  --white:#fff;
}
*{margin:0;padding:0;box-sizing:border-box}
html,body{width:1200px;height:1000px;overflow:hidden;background:var(--white);font-family:'Raleway',sans-serif;color:var(--ink)}
.page{position:relative;width:1200px;height:1000px}
.site{position:absolute;left:252px;top:0;width:696px;height:1000px}

/* header */
.masthead{position:absolute;left:0;top:0;width:696px;height:84px;background:var(--charcoal);border-top:2px solid var(--orange)}
.masthead-centre{position:absolute;left:0;top:0}
.brand{position:absolute;left:296px;top:28px;width:104px;text-align:center;color:var(--white)}
.brand-mark{display:block;width:26px;height:26px;margin:0 auto 6px;background:var(--orange)}
.brand-name{font-size:12px;font-weight:400;letter-spacing:4px}
.phone{position:absolute;left:48px;top:33px;display:flex;align-items:center;gap:8px;color:var(--white);font-size:13px;letter-spacing:.5px}
.socials{position:absolute;right:46px;top:32px;display:flex;gap:11px}
.socials span{width:21px;height:21px;border:1.5px solid #ddd;border-radius:50%}

/* nav */
.main-nav{position:absolute;left:0;top:84px;width:696px;height:27px;display:flex;border-bottom:1px solid var(--line);background:var(--white)}
.main-nav a{display:flex;align-items:center;justify-content:center;font-size:10px;font-weight:500;color:var(--ink);text-decoration:none;letter-spacing:.3px;border-right:1px solid var(--line)}
.main-nav a:last-child{border-right:none}

/* hero */
.hero{position:absolute;left:0;top:111px;width:696px;height:270px;background:linear-gradient(180deg,var(--orange) 0%,var(--orange) 55%,var(--orange-deep) 100%);overflow:hidden}
.hero-glow{position:absolute;left:150px;top:150px;width:260px;height:200px;border-radius:50%;background:radial-gradient(circle,rgba(120,40,0,.35),rgba(120,40,0,0) 70%)}
.hero-title{position:absolute;left:46px;top:58px;color:var(--white);font-weight:300;font-size:21px;line-height:24px}
.hero-copy{position:absolute;left:46px;top:116px;width:255px;color:var(--white);font-size:8.5px;line-height:12.5px}
.btn{position:absolute;left:46px;top:179px;width:76px;height:26px;background:var(--amber);border:1px solid #fff3;color:var(--white);font-size:9.5px;display:flex;align-items:center;justify-content:center;border-radius:2px}
.slide-back{position:absolute;top:32px;width:40px;height:184px;border:2px solid var(--white);border-radius:6px;background:linear-gradient(#3aa0d8,#1f5a86)}
.slide-main{position:absolute;left:338px;top:26px;width:322px;height:206px;border:2px solid var(--white);border-radius:6px;background:linear-gradient(135deg,#1a2a3a 0%,#2f6d8f 45%,#9ab6c8 100%);box-shadow:0 2px 8px rgba(0,0,0,.3)}
.slider-dots{position:absolute;left:488px;top:246px;display:flex;gap:6px;align-items:center}
.slider-dots i{width:4px;height:4px;border-radius:50%;background:var(--white)}
.slider-dots i.on{width:6px;height:6px;border:1px solid var(--white);background:transparent}

/* audience */
.audience-head{position:absolute;left:0;top:408px;width:696px;text-align:center}
.audience-head h2{font-weight:400;font-size:21px;color:var(--ink)}
.audience-head p{margin:12px auto 0;width:600px;font-size:13px;line-height:16px;color:var(--ink)}
.role{position:absolute;top:566px;width:144px;height:249px;border:1px solid var(--line)}
.role-hex{position:absolute;top:500px;width:104px;height:120px}
.role h3{position:absolute;left:0;width:100%;text-align:center;color:var(--orange);font-weight:500;font-size:13px;line-height:15px}
.role p{position:absolute;left:8px;right:8px;top:95px;text-align:center;font-size:7.2px;line-height:10.3px;color:var(--muted)}

/* footer */
.site-footer{position:absolute;left:0;top:863px;width:696px;height:137px;background:linear-gradient(180deg,#1a1a1a,var(--footer))}
.foot-col{position:absolute;top:22px}
.foot-col h4{color:var(--orange);font-size:9.5px;font-weight:700;margin-bottom:6px}
.foot-col li{list-style:none;color:#aaa;font-size:7.5px;line-height:15px}
.foot-div{position:absolute;top:12px;width:1px;height:105px;background:#333}
.contact{position:absolute;left:526px;top:22px}
.contact div{display:flex;gap:8px;color:#aaa;font-size:7.5px;line-height:11px;margin-bottom:10px}
.legal{position:absolute;left:0;bottom:0;width:696px;height:20px;border-top:1px solid #2a2a2a;text-align:center;color:#999;font-size:6px;line-height:20px}
</style>
</head>
<body>
<div class="page">
<div class="site">

  <header class="masthead">
    <svg class="masthead-centre" width="696" height="82" viewBox="0 0 696 82">
      <polygon points="188,0 510,0 465,82 238,82" fill="var(--slate)"/>
    </svg>
    <div class="phone">
      <svg width="18" height="18" viewBox="0 0 18 18"><circle cx="9" cy="9" r="8" fill="none" stroke="#ddd" stroke-width="1.3"/><path d="M6.5 5.5c-.5.5-.5 1.5.5 3.2s2.3 2.8 3.3 3l1.2-1.1-1.4-1.2-.8.6c-.7-.4-1.4-1.2-1.8-2l.6-.8-1-1.4z" fill="#fff"/></svg>
      <span>+44 20 7946 0182</span>
    </div>
    <div class="brand"><span class="brand-mark"></span><span class="brand-name">VELTRA</span></div>
    <div class="socials"><span></span><span></span><span></span><span></span></div>
  </header>

  <nav class="main-nav">
    <a style="width:116px">HOME</a>
    <a style="width:109px">ABOUT</a>
    <a style="width:116px">SERVICES</a>
    <a style="width:119px">PARTNERS</a>
    <a style="width:110px">CLIENTS</a>
    <a style="width:126px">CONTACT</a>
  </nav>

  <section class="hero">
    <div class="hero-glow"></div>
    <h1 class="hero-title">You need integration.<br>We're always there with you.</h1>
    <p class="hero-copy">Veltra is one of the leading systems integrators to the world's finance sector. We are an extension of your business and our services portfolio has been built so you always have access to a complete partner.</p>
    <div class="btn">Read More</div>
    <div class="slide-back" style="left:314px"></div>
    <div class="slide-back" style="left:642px"></div>
    <div class="slide-main" role="img" aria-label="Slide image: business network of connected devices and data above a tablet"></div>
    <div class="slider-dots"><i></i><i class="on"></i><i></i><i></i></div>
  </section>

  <section class="audience-head">
    <h2>Who Are You?</h2>
    <p>If you're part of a financial organisation, we have the power to help everyone work more efficiently, productively and profitably.</p>
  </section>

  <article class="role" style="left:46px">
    <h3 style="top:56px">Senior Hedge Fund Manager/CEO</h3>
    <p>You need to develop and implement strategies for business growth, while ensuring profitability. You're aware your biggest asset is your staff and a happy workforce is a productive one. Security is a key concern in a changing always-on world and you need to be compliant, but you don't want to overspend. Veltra can help you find the best solutions to help your business grow at the speed you want it to.</p>
  </article>
  <article class="role" style="left:199px">
    <h3 style="top:60px">CFO</h3>
    <p>Your key responsibility is to obtain the maximum ROI from products and services. You understand investment opportunities, providing they return higher efficiencies and revenues. You are concerned more with long-term spending versus short-term and how you can get the most value out of a proposition. Veltra can advise how to boost ROI by streamlining your business to maximise return.</p>
  </article>
  <article class="role" style="left:353px">
    <h3 style="top:60px">IT Manager/CTO</h3>
    <p>Integration with partners and services is your key concern. You want to make sure any IT system you implement will work with the whole infrastructure of your company. You don't want your team to waste valuable time dealing with things that don't matter. Veltra provides the whole picture to ensure your company is ready for the next generation of IT.</p>
  </article>
  <article class="role" style="left:506px">
    <h3 style="top:60px">Employees</h3>
    <p>You're working hard, but not getting anywhere fast. You want the tools to make your job easier so you can spend more time thinking about what you're doing rather than how you're doing it. You shouldn't have to think about the technology you're using, because it should just work. Veltra can help you get back on track everyday.</p>
  </article>

  <svg class="role-hex" style="left:67px" viewBox="0 0 104 120"><polygon points="52,0 104,30 104,90 52,120 0,90 0,30" fill="var(--orange)"/><circle cx="52" cy="60" r="26" fill="#f8a267" role="img" aria-label="Icon: executive figure"/></svg>
  <svg class="role-hex" style="left:220px" viewBox="0 0 104 120"><polygon points="52,0 104,30 104,90 52,120 0,90 0,30" fill="var(--orange)"/><circle cx="52" cy="60" r="26" fill="#f8a267" role="img" aria-label="Icon: finance officer with money bag"/></svg>
  <svg class="role-hex" style="left:373px" viewBox="0 0 104 120"><polygon points="52,0 104,30 104,90 52,120 0,90 0,30" fill="var(--orange)"/><circle cx="52" cy="60" r="26" fill="#f8a267" role="img" aria-label="Icon: technology manager with globe network"/></svg>
  <svg class="role-hex" style="left:526px" viewBox="0 0 104 120"><polygon points="52,0 104,30 104,90 52,120 0,90 0,30" fill="var(--orange)"/><circle cx="52" cy="60" r="26" fill="#f8a267" role="img" aria-label="Icon: group of employees"/></svg>

  <footer class="site-footer">
    <div class="foot-col" style="left:49px"><h4>COMPANY</h4><ul><li>› About Us</li><li>› Clients</li></ul></div>
    <div class="foot-div" style="left:141px"></div>
    <div class="foot-col" style="left:177px"><h4>OVERVIEW</h4><ul><li>› What we Do</li><li>› News</li></ul></div>
    <div class="foot-div" style="left:254px"></div>
    <div class="foot-col" style="left:279px"><h4>RESOURCES</h4><ul><li>› Nexora Summary Brochure</li><li>› Nexora Feature Summary</li></ul></div>
    <div class="foot-div" style="left:399px"></div>
    <div class="foot-col" style="left:420px"><h4>NAVIGATION</h4><ul><li>› About</li><li>› Services</li><li>› Partners</li><li>› Clients</li><li>› Contact</li></ul></div>
    <div class="foot-div" style="left:511px"></div>
    <div class="contact">
      <div><svg width="9" height="12" viewBox="0 0 9 12"><path d="M4.5 0A4.5 4.5 0 0 0 0 4.5C0 8 4.5 12 4.5 12S9 8 9 4.5A4.5 4.5 0 0 0 4.5 0z" fill="var(--orange)"/><circle cx="4.5" cy="4.5" r="1.6" fill="#111"/></svg><span>18 Harlow Court, Marylebone,<br>London W1A 4QT</span></div>
      <div><svg width="9" height="11" viewBox="0 0 9 11"><rect x="1" y="0" width="7" height="11" rx="1.2" fill="var(--orange)"/><rect x="2.3" y="1.5" width="4.4" height="6" fill="#111"/></svg><span>+44 20 7946 0182</span></div>
      <div><svg width="10" height="10" viewBox="0 0 10 10"><rect x="0" y="3" width="10" height="7" rx="1" fill="var(--orange)"/><rect x="2" y="0" width="6" height="3" fill="var(--orange)"/></svg><span>+44 20 7946 0183</span></div>
      <div><svg width="10" height="10" viewBox="0 0 10 10"><circle cx="5" cy="5" r="4.5" fill="var(--orange)"/><path d="M0.5 5h9M5 .5c-2 2.5-2 6.5 0 9M5 .5c2 2.5 2 6.5 0 9" stroke="#111" stroke-width=".8" fill="none"/></svg><span>www.veltra-example.co.uk</span></div>
    </div>
    <div class="legal">© Veltra Limited - Company Registration No. 0000000. Incorporated in England and Wales</div>
  </footer>

</div>
</div>
</body>
</html>
```